Business Card Design

After a corporate career in the finance sector I am now operating on my own as a consultant. I require a simple design, and want a strong card which is targeted at a conservative audience.

Target Market(s)

highly educated senior management, directors of companies, finance sector

Industry/Entity Type

Conservative

Contact Information for Business Card

Rosa Tindell
Consultant
Mobile: 0417 862 254
Email: rosa.tind@mailvora.com

Requirements
Should not have
• I don't want the colours green/yellow/brown

```html
<!DOCTYPE html>
<html lang="en">
<head>
<meta charset="utf-8">
<title>Rosa Tindell Consultant – Business Card</title>
<link rel="stylesheet" href="https://fonts.googleapis.com/css2?family=Open+Sans:wght@400;600&family=Teko:wght@500&display=swap">
<style>
  :root {
    --page-bg: #e9e9ec;
    --card-white: #ffffff;
    --card-shade: #e4e4e6;
    --brand-purple: #6a2d8f;
    --brand-purple-light: #8a45b3;
    --swoosh-grey: #3a3a3c;
    --ink-dark: #2b2b2d;
    --ink-mid: #4a4a4d;
  }
  * { margin: 0; padding: 0; box-sizing: border-box; }
  html, body {
    width: 1200px; height: 800px; overflow: hidden;
    background: var(--page-bg);
  }
  .stage {
    width: 1200px; height: 800px;
    display: flex; align-items: center; justify-content: center;
  }
  .business-card {
    position: relative;
    width: 840px; height: 480px;
    background: var(--brand-purple);
    box-shadow: 0 10px 30px rgba(0,0,0,0.18);
    overflow: hidden;
    font-family: "Open Sans", Arial, sans-serif;
  }
  .card-shapes {
    position: absolute; inset: 0;
  }
  .brand-lockup {
    position: absolute; left: 44px; top: 62px;
    display: flex; align-items: center; gap: 16px;
  }
  .brand-square {
    width: 50px; height: 50px;
    background: var(--brand-purple);
    border-radius: 6px;
  }
  .brand-name {
    font-family: "Teko", "Arial Narrow", sans-serif;
    font-weight: 500;
    font-size: 46px; line-height: 1;
    letter-spacing: 1px;
    text-transform: uppercase;
    color: var(--ink-dark);
    padding-top: 8px;
  }
  .person {
    position: absolute; left: 44px; top: 228px;
  }
  .person-name {
    font-weight: 600; font-size: 25px;
    color: var(--brand-purple);
  }
  .person-title {
    font-size: 23px; color: var(--ink-mid);
    margin-top: -2px;
  }
  .contact {
    position: absolute; left: 44px; top: 330px;
    font-size: 16px; color: var(--ink-dark);
  }
  .contact-address { margin-bottom: 8px; }
  .contact-grid {
    display: grid; grid-template-columns: 150px auto;
    row-gap: 6px; column-gap: 22px;
  }
  .contact-item { display: flex; align-items: center; gap: 8px; }
  .contact-icon { width: 15px; height: 15px; flex: none; fill: var(--brand-purple); }
</style>
</head>
<body>
<main class="stage">
  <article class="business-card">
    <svg class="card-shapes" viewBox="0 0 840 480" aria-hidden="true">
      <defs>
        <radialGradient id="face-gradient" cx="0.45" cy="0.4" r="0.75">
          <stop offset="0" stop-color="var(--card-white)"/>
          <stop offset="1" stop-color="var(--card-shade)"/>
        </radialGradient>
        <linearGradient id="band-gradient" x1="0" y1="0" x2="1" y2="0">
          <stop offset="0" stop-color="var(--brand-purple-light)"/>
          <stop offset="1" stop-color="var(--brand-purple)"/>
        </linearGradient>
      </defs>
      <rect class="purple-band" width="840" height="480" fill="url(#band-gradient)"/>
      <path class="grey-swoosh" d="M0,0 H690 C830,150 800,370 665,480 H0 Z"
            fill="var(--swoosh-grey)" stroke="#ffffff" stroke-width="6"/>
      <path class="card-face" d="M0,0 H690 C800,120 790,330 560,480 H0 Z"
            fill="url(#face-gradient)"/>
    </svg>

    <div class="brand-lockup">
      <div class="brand-square"></div>
      <div class="brand-name">Rosa Tindell Consultant</div>
    </div>

    <div class="person">
      <div class="person-name">Corin Halvey</div>
      <div class="person-title">Consultant</div>
    </div>

    <div class="contact">
      <div class="contact-address">12 Alder Court, Level 4, Kessel Road</div>
      <div class="contact-grid">
        <div class="contact-item">
          <svg class="contact-icon" viewBox="0 0 16 16"><path d="M3.6 1.2 6 3.6 4.8 5.6c.9 2.2 3.4 4.7 5.6 5.6l2-1.2 2.4 2.4-1.8 2.2C7 14.4 1.6 9 1.4 3z"/></svg>
          <span>021 604 3178</span>
        </div>
        <div class="contact-item">
          <svg class="contact-icon" viewBox="0 0 16 16"><path d="M1 4h14v4H1z"/><path d="M1 6h14v9H1z"/><rect x="4" y="9" width="8" height="4" fill="#fff"/></svg>
          <span>hello@tindellconsult.net</span>
        </div>
        <div class="contact-item">
          <svg class="contact-icon" viewBox="0 0 16 16"><path d="M1 5h3v10H1zM5 3h9v12H5z"/><rect x="7" y="5" width="5" height="3" fill="#fff"/></svg>
          <span>021 604 3179</span>
        </div>
        <div class="contact-item">
          <svg class="contact-icon" viewBox="0 0 16 16"><circle cx="8" cy="8" r="7"/><path d="M1 8h14M8 1c3 3.5 3 10.5 0 14M8 1c-3 3.5-3 10.5 0 14" stroke="#fff" stroke-width="1" fill="none"/></svg>
          <span>www.tindellconsult.net</span>
        </div>
      </div>
    </div>
  </article>
</main>
</body>
</html>
```